Verndale Harbor Partners

Please look at the logo that we've just received and based on it provide us with the business card designs.

Industry/Entity Type

Business

Requirements
Must have
• Dummy text, so later on we can add the exact names and titles.

```html
<!DOCTYPE html>
<html lang="en">
<head>
<meta charset="utf-8">
<title>Verndale Harbor Partners – Business Cards</title>
<link rel="stylesheet" href="https://fonts.googleapis.com/css2?family=Cinzel:wght@400&family=Roboto:wght@400&display=swap">
<style>
  :root{
    --bg:#e8e5e1;
    --card:#f6f6f6;
    --blue:#1b3a8a;
    --grey:#8c8c8c;
    --text:#3a3a3a;
    --rule:#9a9a9a;
    --white:#ffffff;
  }
  *{margin:0;padding:0;box-sizing:border-box}
  html,body{width:1200px;height:776px;overflow:hidden;background:var(--bg)}
  .canvas{position:relative;width:1200px;height:776px}
  .card{position:absolute;width:485px;height:277px;box-shadow:0 3px 8px rgba(0,0,0,.25);overflow:hidden}
  .card--front{background:var(--card);top:108px}
  .card--front.left{left:103px}
  .card--front.right{left:612px}
  .card--back{background:var(--blue);left:357px;top:404px}

  .brand{position:absolute;right:30px;top:46px;display:flex;align-items:center;gap:8px;
    font-family:"Cinzel",serif;font-weight:400;color:var(--blue);font-size:15px;letter-spacing:.5px}
  .brand__mark{width:12px;height:12px;background:var(--blue)}

  .person{position:absolute;left:31px;top:140px;font-family:"Cinzel",serif;font-weight:400}
  .person__name{color:var(--blue);font-size:19px;line-height:22px}
  .person__title{color:#666;font-size:13.5px;letter-spacing:.6px;line-height:16px}
  .rule{position:absolute;left:31px;right:30px;top:183px;height:1px;background:var(--rule)}

  .contacts{position:absolute;left:31px;top:190px;list-style:none;font-family:"Roboto",sans-serif;
    font-size:11.5px;color:var(--text);line-height:15.5px}
  .contacts li{display:flex;align-items:center;gap:7px}
  .contacts svg{width:10px;height:10px;fill:var(--blue)}

  .address{position:absolute;right:30px;top:206px;text-align:right;font-family:"Roboto",sans-serif;
    font-size:11.5px;color:var(--text);line-height:15px}

  .footer-band{position:absolute;left:0;bottom:0;width:100%;height:10px;background:var(--grey)}
  .footer-web{position:absolute;right:0;bottom:0;width:218px;height:29px;background:var(--blue);
    clip-path:polygon(20px 0,100% 0,100% 100%,0 100%);
    font-family:"Roboto",sans-serif;font-size:11.5px;color:var(--white);letter-spacing:2.4px;
    display:flex;align-items:center;justify-content:flex-end;padding-right:26px}

  .back-brand{position:absolute;left:0;right:0;top:116px;display:flex;justify-content:center;align-items:center;gap:10px;
    font-family:"Cinzel",serif;font-weight:400;color:var(--white);font-size:20px;letter-spacing:1px}
  .back-brand__mark{width:14px;height:14px;background:var(--white)}
  .back-web{position:absolute;left:0;right:0;top:229px;text-align:center;font-family:"Roboto",sans-serif;
    font-size:11.5px;color:var(--white);letter-spacing:8.5px}
</style>
</head>
<body>
<main class="canvas">

  <section class="card card--front left">
    <div class="brand"><span class="brand__mark"></span>VERNDALE HARBOR PARTNERS</div>
    <div class="person">
      <div class="person__name">DANA WHITCOMBE, FCPA</div>
      <div class="person__title">MANAGING PARTNER</div>
    </div>
    <div class="rule"></div>
    <ul class="contacts">
      <li><svg viewBox="0 0 10 10"><path d="M2 0l2 2-1 1.5c.6 1.3 1.4 2.1 2.5 2.5L7 5l2 2-1.3 1.8C4.5 8.8 1 5.5 1 1.3z"/></svg>604-555-0142</li>
      <li><svg viewBox="0 0 10 10"><path d="M2.5 0h5v10h-5zM3.5 1v7h3V1z"/></svg>604-555-0187</li>
      <li><svg viewBox="0 0 10 10"><path d="M0 2h10v6H0zM1 3v.3l4 2.5 4-2.5V3z"/></svg>dwhitcombe@verndalehp.com</li>
    </ul>
    <div class="address">410 - 875 Harbour Lane<br>Seaview BC&nbsp; V0N 2K1</div>
    <div class="footer-band"></div>
    <div class="footer-web">www.verndalehp.com</div>
  </section>

  <section class="card card--front right">
    <div class="brand"><span class="brand__mark"></span>VERNDALE HARBOR PARTNERS</div>
    <div class="person">
      <div class="person__name">OWEN PRESCOTT</div>
      <div class="person__title">MANAGING PARTNER</div>
    </div>
    <div class="rule"></div>
    <ul class="contacts">
      <li><svg viewBox="0 0 10 10"><path d="M2 0l2 2-1 1.5c.6 1.3 1.4 2.1 2.5 2.5L7 5l2 2-1.3 1.8C4.5 8.8 1 5.5 1 1.3z"/></svg>778-555-0163</li>
      <li><svg viewBox="0 0 10 10"><path d="M2.5 0h5v10h-5zM3.5 1v7h3V1z"/></svg>778-555-0129</li>
      <li><svg viewBox="0 0 10 10"><path d="M0 2h10v6H0zM1 3v.3l4 2.5 4-2.5V3z"/></svg>oprescott@verndalehp.com</li>
    </ul>
    <div class="address">410 - 875 Harbour Lane<br>Seaview BC&nbsp; V0N 2K1</div>
    <div class="footer-band"></div>
    <div class="footer-web">www.verndalehp.com</div>
  </section>

  <section class="card card--back">
    <div class="back-brand"><span class="back-brand__mark"></span>VERNDALE HARBOR PARTNERS</div>
    <div class="back-web">www.verndalehp.com</div>
  </section>

</main>
</body>
</html>
```